Screendesign für neue Website
Zielgruppe
Bauherren und alle die mal zum Architekten müssen.
Aufgabenstellung
Bei diesem Auftrag handelt es sich um die Erstellung eines Screendesigns für eine Website eines Archtiktenbüros.
Es wird daher ein Layout im PSD-Format erwartet, eine Umsetzung dessen in HTML wird nicht gefordert.

```html
<!DOCTYPE html>
<html lang="de">
<head>
<meta charset="utf-8">
<title>Planungsbüro Roth – Architekten</title>
<link rel="stylesheet" href="https://fonts.googleapis.com/css2?family=Fira+Sans:wght@400;500;600;700&display=swap">
<style>
  :root {
    --ink: #111111;
    --bar: #050505;
    --paper: #ffffff;
    --green: #2fc42c;
    --frame: #3a3a3a;
    --muted: #6f6f6f;
    --menu: #1a1a1a;
    --chevron: #b9b9b9;
    --floor-dark: #0c0706;
    --floor-mid: #4a3127;
    --floor-light: #7a5747;
  }
  * { box-sizing: border-box; margin: 0; padding: 0; }
  html, body { width: 1200px; height: 840px; overflow: hidden; background: var(--paper); }
  body { font-family: "Fira Sans", Arial, sans-serif; color: var(--ink); position: relative; }

  .topbar {
    position: absolute; left: 0; top: 0; width: 1200px; height: 40px;
    background: linear-gradient(#000 0, #000 34px, #555 40px);
  }
  .topbar__nav {
    position: absolute; right: 42px; top: 13px;
    font-size: 12px; font-weight: 600; color: #fff; letter-spacing: .3px;
  }
  .topbar__nav a { color: #fff; text-decoration: none; }

  .stage {
    position: absolute; left: 0; top: 40px; width: 1200px; height: 624px;
    background:
      radial-gradient(ellipse 560px 70px at 600px 200px, rgba(0,0,0,.28), transparent 70%),
      linear-gradient(#d8d8d8 0, #fff 30px, #fff 100%);
  }

  .gallery__arrow {
    position: absolute; top: 112px; font-size: 52px; line-height: 1;
    color: var(--chevron); font-weight: 400;
  }
  .gallery__arrow--prev { left: 10px; }
  .gallery__arrow--next { right: 10px; }

  .gallery {
    position: absolute; left: 57px; top: 24px; width: 1086px; height: 163px;
    background: var(--frame); padding: 7px 6px; display: flex; gap: 4px;
  }
  .gallery__shot { flex: 1; height: 149px; }
  .shot--houses { background: linear-gradient(#4d7fc4 0, #b9cde6 40%, #e9dfd6 65%, #b27b5c 100%); }
  .shot--villa { background: linear-gradient(#5f8fd0 0, #c5d8ee 35%, #9a8775 60%, #4f7d3a 85%, #5d5d5d 100%); }
  .shot--interior { background: linear-gradient(135deg, #f4f4f4, #c9c9c9 60%, #eaeaea); }
  .shot--model { background: linear-gradient(160deg, #eeeeee, #b5b5b5 70%, #dcdcdc); }

  .claim { position: absolute; font-weight: 600; color: var(--green); font-size: 27px; white-space: nowrap; }
  .claim__box {
    display: inline-block; background: var(--ink); color: #fff; padding: 2px 8px 4px;
    box-shadow: 0 0 12px rgba(0,0,0,.55);
  }
  .claim--1 { left: 140px; top: 264px; }
  .claim--2 { left: 309px; top: 344px; }
  .claim--3 { left: 428px; top: 428px; }
  .claim--4 { left: 546px; top: 511px; }

  .menu { position: absolute; left: 843px; top: 238px; list-style: none; }
  .menu__item { position: relative; padding-left: 25px; height: 62px; }
  .menu__item svg { position: absolute; left: 0; top: 8px; }
  .menu__title { font-size: 21px; font-weight: 400; color: var(--menu); line-height: 1.1; }
  .menu__sub { font-size: 13px; color: var(--muted); margin-top: 2px; }

  .floor {
    position: absolute; left: 0; top: 664px; width: 1200px; height: 176px;
    background:
      radial-gradient(ellipse 520px 120px at 600px 20px, var(--floor-light), transparent 75%),
      linear-gradient(var(--floor-mid), var(--floor-dark) 85%);
  }
  .floor::before {
    content: ""; position: absolute; left: 0; top: 0; width: 100%; height: 10px;
    background: linear-gradient(#bbb, #3a2a24);
  }

  .brandcard {
    position: absolute; left: 96px; top: 525px; width: 259px; height: 207px;
    border-radius: 12px; background: linear-gradient(#fafafa, #cfcfcf);
    box-shadow: 0 4px 18px rgba(0,0,0,.6);
    display: flex; flex-direction: column; align-items: center; justify-content: center; gap: 14px;
  }
  .brandcard__square { width: 44px; height: 44px; background: var(--ink); }
  .brandcard__name { font-size: 19px; font-weight: 600; color: var(--ink); text-align: center; line-height: 1.25; }

  .copyright {
    position: absolute; right: 42px; bottom: 18px; font-size: 12px; color: #fff; font-weight: 500;
  }
</style>
</head>
<body>
  <header class="topbar">
    <nav class="topbar__nav"><a href="#">HOME</a> | <a href="#">KONTAKT</a> | <a href="#">IMPRESSUM</a></nav>
  </header>

  <main class="stage">
    <span class="gallery__arrow gallery__arrow--prev">«</span>
    <div class="gallery">
      <div class="gallery__shot shot--houses" role="img" aria-label="Foto: Reihenhäuser unter blauem Himmel"></div>
      <div class="gallery__shot shot--villa" role="img" aria-label="Foto: Einfamilienhaus mit Rasen und Einfahrt"></div>
      <div class="gallery__shot shot--interior" role="img" aria-label="Visualisierung: heller Wohnraum"></div>
      <div class="gallery__shot shot--model" role="img" aria-label="Visualisierung: Gittermodell eines Innenraums"></div>
      <div class="gallery__shot shot--houses" role="img" aria-label="Foto: Reihenhäuser unter blauem Himmel"></div>
    </div>
    <span class="gallery__arrow gallery__arrow--next">»</span>

    <p class="claim claim--1">Architekten schaffen</p>
    <p class="claim claim--2">Lebens - <span class="claim__box">Raum</span></p>
    <p class="claim claim--3">Lebens - <span class="claim__box">Traum</span></p>
    <p class="claim claim--4">Traum - <span class="claim__box">Haus</span></p>

    <ul class="menu">
      <li class="menu__item"><svg width="16" height="10" viewBox="0 0 16 10"><path d="M1 1l5 4-5 4M8 1l5 4-5 4" fill="none" stroke="#777" stroke-width="1.5"/></svg><div class="menu__title">Unternehmen</div><div class="menu__sub">Erfahren Sie mehr über uns...</div></li>
      <li class="menu__item"><svg width="16" height="10" viewBox="0 0 16 10"><path d="M1 1l5 4-5 4M8 1l5 4-5 4" fill="none" stroke="#777" stroke-width="1.5"/></svg><div class="menu__title">Projekte</div><div class="menu__sub">Projekte im Überblick...</div></li>
      <li class="menu__item"><svg width="16" height="10" viewBox="0 0 16 10"><path d="M1 1l5 4-5 4M8 1l5 4-5 4" fill="none" stroke="#777" stroke-width="1.5"/></svg><div class="menu__title">Information</div><div class="menu__sub">Allgemein, Standort...</div></li>
      <li class="menu__item"><svg width="16" height="10" viewBox="0 0 16 10"><path d="M1 1l5 4-5 4M8 1l5 4-5 4" fill="none" stroke="#777" stroke-width="1.5"/></svg><div class="menu__title">Aktuelles</div><div class="menu__sub">Neue Vorhaben, Förderung...</div></li>
      <li class="menu__item"><svg width="16" height="10" viewBox="0 0 16 10"><path d="M1 1l5 4-5 4M8 1l5 4-5 4" fill="none" stroke="#777" stroke-width="1.5"/></svg><div class="menu__title">Leistungen</div><div class="menu__sub">Planung, Baubetreung, etc...</div></li>
      <li class="menu__item"><svg width="16" height="10" viewBox="0 0 16 10"><path d="M1 1l5 4-5 4M8 1l5 4-5 4" fill="none" stroke="#777" stroke-width="1.5"/></svg><div class="menu__title">Kontakt</div><div class="menu__sub">Unsere Kontaktdaten...</div></li>
    </ul>
  </main>

  <footer class="floor" role="img" aria-label="Dunkler Parkettboden im Fischgrätmuster">
    <p class="copyright">© Planungsbüro Roth 2010</p>
  </footer>

  <div class="brandcard">
    <span class="brandcard__square"></span>
    <span class="brandcard__name">Planungsbüro<br>Anselm Roth</span>
  </div>
</body>
</html>
```